Website Design for Car Donations

Revise current site www.wheelsforheroes-sample.org

Sites i like:

https://www.autogiftbrigade.example

https://ridegivingcorps.example

https://protoboardly.example/7a2d91e4/screen/58217046

```html
<!DOCTYPE html>
<html lang="en">
<head>
<meta charset="utf-8">
<title>Wheels for Heroes – Donate Your Car</title>
<link href="https://fonts.googleapis.com/css2?family=Exo+2:ital,wght@0,400;0,600;0,800;1,400;1,600;1,800;1,900&display=swap" rel="stylesheet">
<style>
:root{
  --navy:#0a2a86;
  --navy-dark:#061d5e;
  --red:#c4150f;
  --red-dark:#9d0f0b;
  --black:#0b0b0f;
  --paper:#efefef;
  --ink:#222;
  --muted:#777;
  --white:#fff;
}
*{box-sizing:border-box;margin:0;padding:0}
html,body{width:775px;height:1200px;overflow:hidden}
body{position:relative;font-family:"Exo 2",sans-serif;background:var(--white);color:var(--ink)}
.abs{position:absolute}

/* header */
.site-header{left:0;top:0;width:775px;height:50px;background:var(--red)}
.site-header .blue{left:0;top:0;width:775px;height:50px}
.brand{left:112px;top:13px;display:flex;align-items:center;gap:6px;font-weight:800;font-size:14px;color:var(--white);letter-spacing:.3px}
.brand .dot{width:14px;height:14px;border-radius:50%;background:var(--white)}
.main-nav{right:112px;top:21px;display:flex;gap:16px;font-size:8.5px;font-weight:600;color:var(--white)}

/* hero */
.hero-photo{left:0;top:50px;width:775px;height:312px;background:linear-gradient(100deg,#2a2f4a 0%,#5a4a3e 30%,#7a2a2a 60%,#3a1418 100%)}
.donate-form{left:408px;top:62px;width:255px;height:288px;background:rgba(0,0,0,.55);border:1px solid rgba(255,255,255,.35);padding:10px 12px}
.donate-form h2{font-style:italic;font-weight:800;font-size:17px;color:var(--white);text-align:center;line-height:1.1}
.donate-form .sub{font-style:italic;font-size:10px;color:var(--white);text-align:center;margin:2px 0 8px}
.field{height:24px;background:var(--white);margin-bottom:4.5px;font-size:6.5px;font-style:italic;color:#555;padding:0 8px;display:flex;align-items:center;justify-content:space-between}
.field-row{display:flex;gap:5px}
.field-row .field{flex:1}
.caret{width:0;height:0;border-left:3px solid transparent;border-right:3px solid transparent;border-top:4px solid var(--red)}
.btn{margin-top:8px;height:28px;background:var(--red);color:var(--white);font-style:italic;font-weight:600;font-size:10px;display:flex;align-items:center;justify-content:center}
.call-bar{left:113px;top:337px;height:25px;width:252px;display:flex}
.call-bar .label{background:var(--navy);color:var(--white);font-style:italic;font-weight:600;font-size:11px;width:110px;display:flex;align-items:center;justify-content:center}
.call-bar .num{background:var(--red);color:var(--white);font-style:italic;font-weight:800;font-size:16px;flex:1;display:flex;align-items:center;justify-content:center}

/* benefit strip */
.strip{left:0;top:362px;width:775px;height:74px;background:var(--navy)}
.strip-title{left:112px;top:370px;color:var(--white);font-style:italic;font-weight:800;font-size:14px;line-height:1}
.strip-title .big{display:block;color:var(--red);font-size:27px;line-height:1.05}
.benefit{top:372px;width:64px;text-align:center;color:var(--white);font-size:5px;font-weight:800;font-style:italic;line-height:1.3}
.benefit svg{display:block;margin:0 auto 3px}

/* how */
.how{left:0;top:436px;width:775px;height:269px;background:var(--paper)}
.section-title{left:0;width:775px;text-align:center;font-style:italic;font-weight:900;font-size:30px}
.how .section-title{top:26px;color:var(--navy)}
.how .section-title span{color:var(--red)}
.step{top:85px;width:180px;text-align:center}
.step .circle{width:84px;height:84px;border-radius:50%;margin:0 auto;display:flex;align-items:center;justify-content:center}
.step h3{font-style:italic;font-weight:600;font-size:11px;color:var(--black);margin-top:9px;line-height:1.3;text-transform:uppercase}
.step p{font-size:8.5px;color:var(--muted);margin-top:8px;line-height:1.35}

/* why */
.why{left:0;top:705px;width:775px;height:345px;background:linear-gradient(90deg,#1b2346 0%,#384266 35%,#7a2630 65%,#b83a3a 100%)}
.why .section-title{top:36px;color:var(--white);font-size:29px}
.reason{left:155px;width:485px;height:32px}
.reason .star{left:0;top:0;width:44px;height:32px;background:var(--navy)}
.reason .text{left:25px;top:0;width:460px;height:32px;padding:0 30px 0 28px;display:flex;align-items:center;font-style:italic;font-size:10.5px;color:var(--white);line-height:1.3}
.reason b{font-weight:800}

/* footer */
.site-footer{left:0;top:1050px;width:775px;height:122px;background:var(--navy)}
.silhouette{top:0;width:110px;height:122px;background:linear-gradient(180deg,transparent,rgba(6,29,94,.8))}
.foot-col{top:26px;color:var(--white)}
.foot-col h4{font-style:italic;font-weight:800;font-size:10.5px;margin-bottom:9px}
.foot-col p,.foot-col li{font-size:5.8px;line-height:1.35;list-style:none}
.foot-col li{margin-bottom:8px}
.badge{width:60px;height:18px;border-radius:3px;background:rgba(255,255,255,.85);margin-bottom:8px}
.badge.round{width:20px;height:20px;border-radius:50%}
.copyright{left:0;top:1172px;width:775px;height:28px;background:var(--navy-dark);color:var(--white);font-size:6px;display:flex;align-items:center;justify-content:center}
</style>
</head>
<body>

<header class="site-header abs">
  <svg class="blue abs" width="775" height="50"><polygon points="0,0 290,0 272,50 0,50" fill="#0a2a86"/></svg>
  <div class="brand abs"><span class="dot"></span>WHEELS FOR HEROES</div>
  <nav class="main-nav abs"><span>HOW TO DONATE</span><span>WHY DONATE</span><span>FAQ</span><span>ABOUT</span></nav>
</header>

<section>
  <div class="hero-photo abs" role="img" aria-label="Soldier in uniform hugging a child holding a small flag, in front of a large flag"></div>
  <form class="donate-form abs">
    <h2>DONATE YOUR CAR ONLINE</h2>
    <p class="sub">FULL TAX DEDUCTION - RUNNING OR NOT</p>
    <div class="field">FIRST NAME</div>
    <div class="field">LAST NAME</div>
    <div class="field">DAY TIME PHONE</div>
    <div class="field">EMAIL</div>
    <div class="field">ZIP CODE</div>
    <div class="field-row"><div class="field">CHOOSE YEAR<i class="caret"></i></div><div class="field">CHOOSE MAKE<i class="caret"></i></div></div>
    <div class="field">VEHICLE MODEL</div>
    <div class="btn">DONATE NOW</div>
  </form>
  <div class="call-bar abs"><span class="label">CALL TO DONATE</span><span class="num">1-800-555-0142</span></div>
</section>

<section>
  <svg class="strip abs" width="775" height="74"><rect width="775" height="74" fill="#0a2a86"/><polygon points="0,0 287,0 270,74 0,74" fill="#0b0b0f"/></svg>
  <div class="strip-title abs">DONATE YOUR CAR TO<span class="big">VETERANS</span>MAKE A DIFFERENCE</div>
  <div class="benefit abs" style="left:280px"><svg width="38" height="36" viewBox="0 0 38 36"><circle cx="18" cy="18" r="15" fill="none" stroke="#fff" stroke-width="3"/><path d="M11 18l6 6 16-16" fill="none" stroke="#fff" stroke-width="4"/></svg>YOU HAVE NO COSTS</div>
  <div class="benefit abs" style="left:347px"><svg width="38" height="36" viewBox="0 0 38 36"><path d="M6 24h26v-6l-6-6H16v12" fill="none" stroke="#fff" stroke-width="2.5"/><path d="M4 4l10 12" stroke="#fff" stroke-width="2.5"/><circle cx="12" cy="28" r="4" fill="#fff"/><circle cx="27" cy="28" r="4" fill="#fff"/></svg>FREE TOWING, RUNNING OR NOT</div>
  <div class="benefit abs" style="left:412px"><svg width="38" height="36" viewBox="0 0 38 36"><rect x="10" y="2" width="18" height="32" fill="none" stroke="#fff" stroke-width="2.5"/><path d="M14 12h10M14 18h10M14 24h10" stroke="#fff" stroke-width="2"/></svg>WE ISSUE YOU AN IRS TAX RECEIPT</div>
  <div class="benefit abs" style="left:480px"><svg width="38" height="36" viewBox="0 0 38 36"><rect x="12" y="3" width="20" height="28" fill="none" stroke="#fff" stroke-width="2.5"/><circle cx="14" cy="18" r="7" fill="#0a2a86" stroke="#fff" stroke-width="2.5"/><path d="M9 23l-5 6" stroke="#fff" stroke-width="3"/></svg>WE TAKE CARE OF ALL PAPERWORK</div>
  <div class="benefit abs" style="left:543px"><svg width="38" height="36" viewBox="0 0 38 36"><rect x="10" y="4" width="18" height="30" rx="2" fill="none" stroke="#fff" stroke-width="2.5"/><path d="M14 14h10M14 20h10M14 26h10" stroke="#fff" stroke-width="2"/></svg>NO DMV HASSLES</div>
  <div class="benefit abs" style="left:609px"><svg width="38" height="36" viewBox="0 0 38 36"><rect x="4" y="9" width="30" height="24" rx="3" fill="#fff"/><rect x="14" y="3" width="10" height="7" fill="none" stroke="#fff" stroke-width="2.5"/></svg>VACATION VOUCHER</div>
</section>

<section class="how abs">
  <h2 class="section-title abs">HOW TO <span>DONATE</span></h2>
  <div class="step abs" style="left:111px"><div class="circle" style="background:var(--navy)"><svg width="40" height="40" viewBox="0 0 40 40"><rect x="6" y="6" width="22" height="28" fill="none" stroke="#fff" stroke-width="3"/><path d="M11 14h12M11 20h12M11 26h8M22 30l12-12" stroke="#fff" stroke-width="3"/></svg></div><h3>Call us at 1-800-555-0142<br>or fill out the online form</h3><p>Donating your vehicle is easy and donation is accepted nationwide.</p></div>
  <div class="step abs" style="left:298px"><div class="circle" style="background:var(--red)"><svg width="50" height="40" viewBox="0 0 50 40"><path d="M8 28h36v-8l-8-8H22v16" fill="none" stroke="#fff" stroke-width="3"/><path d="M4 6l14 14" stroke="#fff" stroke-width="3"/><circle cx="15" cy="31" r="5" fill="#c4150f" stroke="#fff" stroke-width="3"/><circle cx="37" cy="31" r="5" fill="#c4150f" stroke="#fff" stroke-width="3"/></svg></div><h3>We tow the<br>vehicle</h3><p>Any vehicles are accepted and we will arrange to pick up your vehicle when it is most convenient for you.</p></div>
  <div class="step abs" style="left:489px"><div class="circle" style="background:var(--navy)"><svg width="40" height="44" viewBox="0 0 40 44"><path d="M8 4h24v36l-4-3-4 3-4-3-4 3-4-3-4 3z" fill="none" stroke="#fff" stroke-width="3"/><path d="M13 12h14M13 18h14M13 24h8" stroke="#fff" stroke-width="2.5"/></svg></div><h3>Tax<br>write-off</h3><p>Once the vehicle donation is complete, you will receive your tax deductable vehicle donation receipt.</p></div>
</section>

<section class="why abs" role="img" aria-label="Waving flag in the background">
  <h2 class="section-title abs">WHY DONATE YOUR CAR TO US</h2>
  <div class="reason abs" style="top:90px"><svg class="star abs" width="44" height="32"><rect width="44" height="32" fill="#0a2a86"/><polygon points="17,8 19,14 25,14 20,18 22,24 17,20 12,24 14,18 9,14 15,14" fill="#fff"/></svg><svg class="abs" style="left:25px" width="460" height="32"><polygon points="12,0 460,0 448,32 0,32" fill="#c4150f"/></svg><div class="text abs"><span><b>IRS 501(c)3 Approved :</b> Free 24/7 Pickup with No DMV Hassles.</span></div></div>
  <div class="reason abs" style="top:129px"><svg class="star abs" width="44" height="32"><rect width="44" height="32" fill="#0a2a86"/><polygon points="17,8 19,14 25,14 20,18 22,24 17,20 12,24 14,18 9,14 15,14" fill="#fff"/></svg><svg class="abs" style="left:25px" width="460" height="32"><polygon points="12,0 460,0 448,32 0,32" fill="#c4150f"/></svg><div class="text abs"><span><b>Free Local Towing :</b> We will pick up your car donation, running or not, when it’s most convenient, at home or work.</span></div></div>
  <div class="reason abs" style="top:168px"><svg class="star abs" width="44" height="32"><rect width="44" height="32" fill="#0a2a86"/><polygon points="17,8 19,14 25,14 20,18 22,24 17,20 12,24 14,18 9,14 15,14" fill="#fff"/></svg><svg class="abs" style="left:25px" width="460" height="32"><polygon points="12,0 460,0 448,32 0,32" fill="#c4150f"/></svg><div class="text abs"><span><b>Income Tax Deduction :</b> We issue you an IRS tax receipt and get you the highest tax write-off possible.</span></div></div>
  <div class="reason abs" style="top:208px"><svg class="star abs" width="44" height="32"><rect width="44" height="32" fill="#0a2a86"/><polygon points="17,8 19,14 25,14 20,18 22,24 17,20 12,24 14,18 9,14 15,14" fill="#fff"/></svg><svg class="abs" style="left:25px" width="460" height="32"><polygon points="12,0 460,0 448,32 0,32" fill="#c4150f"/></svg><div class="text abs"><span><b>No Paperwork Hassles :</b> We handle everything: DMV and IRS paperwork.</span></div></div>
  <div class="reason abs" style="top:247px"><svg class="star abs" width="44" height="32"><rect width="44" height="32" fill="#0a2a86"/><polygon points="17,8 19,14 25,14 20,18 22,24 17,20 12,24 14,18 9,14 15,14" fill="#fff"/></svg><svg class="abs" style="left:25px" width="460" height="32"><polygon points="12,0 460,0 448,32 0,32" fill="#c4150f"/></svg><div class="text abs"><span><b>Car donations help fund programs :</b> And benefit Valor Path Foundation. An IRS 501(c)3 nonprofit organization.</span></div></div>
  <div class="reason abs" style="top:287px"><svg class="star abs" width="44" height="32"><rect width="44" height="32" fill="#0a2a86"/><polygon points="17,8 19,14 25,14 20,18 22,24 17,20 12,24 14,18 9,14 15,14" fill="#fff"/></svg><svg class="abs" style="left:25px" width="460" height="32"><polygon points="12,0 460,0 448,32 0,32" fill="#c4150f"/></svg><div class="text abs"><span><b>Schedule a Free Pickup :</b> Complete the form and a representative will call you to arrange a convenient time to pickup your car.</span></div></div>
</section>

<footer class="site-footer abs">
  <div class="silhouette abs" style="left:0" role="img" aria-label="Soldier silhouettes"></div>
  <div class="silhouette abs" style="right:0" role="img" aria-label="Soldier silhouettes"></div>
  <div class="foot-col abs" style="left:112px;width:150px"><h4>ABOUT US</h4><p>Car donations help fund programs and benefit Valor Path Foundation. An IRS 501(c)3 nonprofit organization. Schedule a Free Pickup: Complete the form and a representative will call you to arrange a convenient time to pickup your car.</p></div>
  <div class="foot-col abs" style="left:281px"><h4>NAVIGATION</h4><ul><li>› HOW TO DONATE</li><li>› WHY DONATE</li><li>› FAQ</li><li>› ABOUT</li></ul></div>
  <div class="foot-col abs" style="left:371px"><h4>SAFE &amp; SECURE</h4><div class="badge"></div><div class="badge round"></div></div>
  <div class="foot-col abs" style="left:476px"><h4>YOU’VE GOT QUESTION ?</h4><p style="font-size:8.5px;font-weight:800;font-style:italic">CALL TODAY TO DONATE</p><p style="font-size:15px;font-weight:800;font-style:italic;line-height:1.4">1-800-555-0142</p><p>Live Operators Available - 7 Days A Week</p></div>
</footer>
<div class="copyright abs">© 2018 WHEELS FOR HEROES. PRIVACY POLICY.</div>

</body>
</html>
```